Norwegian Mobile Home/Cabin Producer Needs Brochure Design

We make and deliver our own brand of mobile homes especially made for Norway and it's weather conditions. We differ from other brands in building quality in regards to a much more solid construction, insulation and choices. We work with our customer from the beginning and build them after their demands and wishes.
We need a brochure that holds us out as top of the line. We deliver mobile homes of all kinds and sizes. Both to the private and professional sector.
For the professional sector, mainly camping sites we want to show, lodges-, sanitary- and kitchen wagoons etc.
So we need a brochure of 14-20 pages in A4 where the double pages can be printed in A3 format.
We have logo (provided). But we need cover as well as back suggestions.
It should start with pages where we can teel who we are and stand for.Piicture(s) and space for some editable text (which we can write in norwegian). The text part can have a transparent background......or not. Give us your best shot. Also a smaller part in the private sector that shows winter time.
We want other pages for the private sector that shows what we deliver and the possibilities of choices.
Pages for the the professional sector.
Pages that show our production. How we transport. And the split construction. Only pictures from this portfolio here. (see skydrive portfolios)
Take a look at provided pictures and our website www.solvikvarde.no for inspiration.
Here's a SkyDrive link to Pictures to choose from. http://lnkbox.example/QK41TP
(Hope it Works, let me know if not)
Our company name in small letters "solvikvarde fritidshytter" means directly translated "sunbay cottage shelters".
Looking forward to your suggestions.
Target Market(s)
Private market for vacation mobile homes. Camping sites and similar
Industry/Entity Type
Insulation
Requirements
Must have
- Our logo on the front page. Simple but inviting and professional
Logo and address on the back.

```html
<!DOCTYPE html>
<html lang="no">
<head>
<meta charset="utf-8">
<title>Sikker Transport – hele veien</title>
<link rel="stylesheet" href="https://fonts.googleapis.com/css2?family=Fira+Sans:ital,wght@0,300;0,400;1,300&display=swap">
<style>
  :root{
    --backdrop:#e3e6e9;
    --paper:#ffffff;
    --panel-light:#d8e0e6;
    --panel-mid:#c8d1d8;
    --curve-line:#b3bec7;
    --ink:#3a4047;
    --ink-soft:#5f676e;
  }
  *{box-sizing:border-box;margin:0;padding:0}
  html,body{width:1200px;height:806px;overflow:hidden;background:var(--backdrop)}
  body{font-family:"Fira Sans",Arial,sans-serif;color:var(--ink);position:relative}
  .sheet{position:absolute;left:136px;top:68px;width:960px;height:678px;background:var(--paper)}
  .spread{position:absolute;left:158px;top:91px;width:912px;height:633px;overflow:hidden}
  .spread-art{position:absolute;inset:0}
  .page-title{position:absolute;left:22px;top:62px;font-size:18.5px;font-weight:400;color:var(--ink)}
  .photo-grid{position:absolute;left:22px;top:109px;width:324px;height:283px;display:grid;grid-template-columns:160px 162px;grid-template-rows:141px 140px;gap:2px}
  .photo{background:linear-gradient(180deg,#e4e8ea 0%,#d3d7d6 30%,#cfcd9c 52%,#c4c07a 64%,#bfc1bf 82%,#b3b7b9 100%)}
  .photo-depot{background:linear-gradient(180deg,#e2e6e8 0%,#b9b9a2 32%,#c9c27a 55%,#c7c9b4 72%,#b6babc 100%)}
  .photo-close{background:linear-gradient(180deg,#e7eaec 0%,#dadcda 35%,#c9c47c 58%,#b7b890 76%,#a9adae 100%)}
  .quote{position:absolute;left:10px;top:505px;width:300px;text-align:right;font-size:9.8px;font-style:italic;font-weight:300;line-height:13.5px;color:var(--ink)}
  .column{position:absolute;font-size:7.6px;line-height:10.6px;font-weight:300;color:var(--ink-soft);text-align:justify}
  .column h3{font-size:12px;font-weight:400;color:var(--ink);margin-bottom:4px;text-align:left}
  .column p+h3{margin-top:12px}
  .column p+p{margin-top:10px}
  .column-one{left:498px;top:467px;width:190px}
  .column-two{left:701px;top:484px;width:178px}
</style>
</head>
<body>
  <div class="sheet"></div>
  <section class="spread">
    <svg class="spread-art" viewBox="0 0 912 633" width="912" height="633">
      <defs>
        <linearGradient id="forest-road" x1="0" y1="0" x2="0.35" y2="1">
          <stop offset="0" stop-color="#6f8048"/>
          <stop offset=".35" stop-color="#8a9150"/>
          <stop offset=".6" stop-color="#a8a458"/>
          <stop offset=".82" stop-color="#9fa38a"/>
          <stop offset="1" stop-color="#c9ccc8"/>
        </linearGradient>
      </defs>
      <rect class="panel-left" x="0" y="0" width="912" height="633" fill="var(--panel-light)"/>
      <rect class="panel-right" x="457" y="0" width="455" height="633" fill="var(--panel-mid)"/>
      <path class="swoosh" d="M388,0 C390,110 420,190 470,245 C540,320 650,375 780,393 C830,399 880,401 912,401 L912,0 Z" fill="var(--paper)"/>
      <path class="swoosh-band" d="M446,0 L464,0 C466,130 505,235 590,310 C520,270 448,160 446,0 Z" fill="var(--panel-mid)"/>
      <path class="swoosh-tail" d="M545,345 C625,405 700,435 792,455 C700,440 615,415 545,352 Z" fill="var(--paper)"/>
      <path class="swoosh-line" d="M398,0 C400,140 450,240 540,305 C620,360 720,390 912,404" fill="none" stroke="var(--curve-line)" stroke-width="1"/>
      <path class="hero-photo" role="img" aria-label="Photo: a yellow truck carrying a wooden cabin along a forest road, a worker walking ahead" d="M481,0 L912,0 L912,365 C850,378 780,384 706,377 C620,368 560,330 522,270 C494,220 481,130 481,0 Z" fill="url(#forest-road)"/>
    </svg>

    <h1 class="page-title">Sikker Transport - hele veien</h1>

    <div class="photo-grid">
      <div class="photo" role="img" aria-label="Photo: yellow truck with a mobile home on a low trailer"></div>
      <div class="photo photo-depot" role="img" aria-label="Photo: two yellow trucks parked at a depot"></div>
      <div class="photo photo-close" role="img" aria-label="Photo: truck loaded with a white mobile home, front view"></div>
      <div class="photo photo-close" role="img" aria-label="Photo: second truck with mobile home alongside"></div>
    </div>

    <p class="quote">We believe that quality in a service or product is not what we put<br>into it. It is what our customers gets out of it.”</p>

    <div class="column column-one">
      <h3>Alia Doming Eirmod Eum</h3>
      <p>Movet dolore reprimique ea nec, sea no omnes tantas complectitur. Tale munere salutatus et his, utinam melius tibique nam et. His ut brute illud. Alia doming eirmod eum ei, tollit molestiae vel et. An cibo clita iisque qui, phaedrum moderatius no quo.</p>
      <h3>Ex Inani Argumentum</h3>
      <p>Movet dolore reprimique ea nec, sea no omnes tantas complectitur. Tale munere salutatus et his, utinam melius tibique nam et. His ut brute illud. Alia doming eirmod eu ex inani argumentum appellantur nam, noster graeco vel ei,</p>
    </div>

    <div class="column column-two">
      <p>et quod agam posse per. Has cu quot fastidii dissentiet. Ei cum duis fastidii. Et nam voluptua appetere, cu eos graeco facilis philosophia. Mei appetere forensibus at, timeam facilisis eu quo. Ei cum duis fastidii. Et nam voluptua appetere.</p>
      <p>Ex inani argumentum appellantur nam, noster graeco vel ei, et quod agam posse per. Has cu quot fastidii dissentiet. Ei cum duis fastidii. Et nam voluptua appetere, cu eos graeco facilis philosophia. Mei appetere forensibus at, timeam facilisis eu quo. Ei cum duis fastidii. Et nam voluptua appetere, cu eos graeco facilis philosophia.</p>
    </div>
  </section>
</body>
</html>
```